We need a flyer design for a new fencing business. We do ferrowane fencing instalations and pride our company on Reliabilty, Dependabilty and genuine quality. Because it's not just a fence... It's your fence. Our company offers customer free quotes. Things that would need to be on the flyer;

*Company Name - Valley Copperpath Fencing
*Company email - copperpathfencing@quillmail.net
*Company Phone number - 0455 912 307

*Ferrowane fence specialist
*Free quotes

```html
<!DOCTYPE html>
<html lang="en">
<head>
<meta charset="utf-8">
<title>Valley Copperpath Fencing Flyer</title>
<link href="https://fonts.googleapis.com/css2?family=Open+Sans:wght@600;700;800&display=swap" rel="stylesheet">
<style>
  :root {
    --sky: #00aeef;
    --sun: #fff200;
    --ink: #111111;
    --paper: #ffffff;
    --tag: #1d1d1d;
  }
  * { margin: 0; padding: 0; box-sizing: border-box; }
  html, body { width: 828px; height: 1200px; overflow: hidden; background: var(--paper); }
  body { position: relative; font-family: "Open Sans", Verdana, sans-serif; color: var(--ink); }
  .band { position: absolute; display: flex; flex-direction: column; align-items: center; justify-content: center; text-align: center; }

  .flyer-top-head { left: 7px; top: 26px; width: 810px; height: 236px; background: var(--sky); }
  .flyer-top-contact { left: 7px; top: 262px; width: 810px; height: 159px; background: var(--sun); }
  .flyer-top-slogan { left: 7px; top: 425px; width: 810px; height: 146px; background: var(--sky); }

  .flyer-bottom { left: 15px; top: 634px; width: 805px; height: 469px; background: var(--sun); justify-content: flex-start; padding-top: 38px; }
  .flyer-bottom-bar { left: 15px; top: 1103px; width: 805px; height: 73px; background: var(--sky); }

  .brand-name { font-weight: 800; font-size: 50px; letter-spacing: 1px; color: var(--ink); line-height: 1.1; }
  .brand-tag { font-weight: 700; font-size: 21px; color: var(--tag); letter-spacing: 1px; margin-top: 12px; }

  .quote-call { font-weight: 800; font-size: 33px; letter-spacing: 1px; line-height: 1.2; }
  .quote-phone { font-weight: 800; font-size: 33px; letter-spacing: 3px; line-height: 1.2; }
  .quote-email { font-weight: 700; font-size: 27px; margin-top: 10px; }

  .slogan { color: var(--paper); font-weight: 600; font-size: 38px; line-height: 1.35; letter-spacing: 2px;
    text-shadow: 0 0 2px #003f5c, 1px 1px 0 #003f5c; }

  .values { list-style: none; margin-top: 26px; }
  .values li { font-weight: 800; font-size: 44px; letter-spacing: 6px; color: var(--sky); line-height: 1.7;
    text-shadow: -1px -1px 0 #005b80, 1px -1px 0 #005b80, -1px 1px 0 #005b80, 1px 1px 0 #005b80; }

  .bar-contact { font-weight: 700; font-size: 27px; letter-spacing: 1px; color: var(--ink); }
</style>
</head>
<body>
  <section class="band flyer-top-head">
    <div class="brand-name">Valley Copperpath Fencing</div>
    <div class="brand-tag">Your Ferrowane Fence Specialist</div>
  </section>
  <section class="band flyer-top-contact">
    <div class="quote-call">Contact us today for your FREE QUOTE!</div>
    <div class="quote-phone">0455 912 307</div>
    <div class="quote-email">copperpathfencing@quillmail.net</div>
  </section>
  <section class="band flyer-top-slogan">
    <p class="slogan">Because it's not just a fence...<br>It's your fence!</p>
  </section>

  <section class="band flyer-bottom">
    <div class="brand-name">Valley Copperpath Fencing</div>
    <div class="brand-tag">Your Ferrowane Fence Specialist</div>
    <ul class="values">
      <li>Reliabilty</li>
      <li>Dependabilty</li>
      <li>Genuine Quality</li>
    </ul>
  </section>
  <section class="band flyer-bottom-bar">
    <div class="bar-contact">0455 912 307 * copperpathfencing@quillmail.net</div>
  </section>
</body>
</html>
```